New Book Cover Design Project for The Lantern Hopper

I need a book cover designed for my book, "9 Bright Paths to Steady Wealth on Your Terms, Leave the Office Grind, and Chase Your Horizon!" The cover needs to include my logo. It's a step by step guide to earning money from home in various different ways. By doing this, people can quit their jobs and live their dream life. A life with purpose, happiness and abundance. I would love an image of a lady in a suit crushing a desk, or of someone sitting on a island or of money abundantly flowing or a combination of all of these things. It needs to represent the dream life and be visually strong to look at. It needs to include the logo at the top. Its important that people identify with it instantly.

Project Deadline Extended Reason: I've extended the deadline as I realised I not provided some key details such as dimensions of the book, author's name plus details for the back cover. Thanks. Added Sunday, August 6, 2017

Target Market(s)

Women over 30 who are fed up with working in a cubicle and of corporate life.

Industry/Entity Type

Entrepreneur

Font styles to use
Other font styles liked:
• Arial Narrow or Century Gothic or something fun!

Colors

Designer to choose colors to be used in the design.

Requirements
Must have
• My logo at the top (non-negotiable). It needs to convey someone living their dreams or quitting their job or crushing their cubicle. I want it to be like no other title. Visually strong, clear and representative of what it is about. This book represents an opportunity for people to transform their lives! I want them to see this book and want to buy it.
Nice to have
• Examples could be leaving their desk and entering through a door to an amazing life. Money could feature somewhere in it. It needs to represent the dream and someone attaining it. It could feature balloons to escape their desk, or climbing out of their desk to an amazing life.
Should not have
• Anything scary! I don't want too many images or confusing images.

```html
<!DOCTYPE html>
<html lang="en">
<head>
<meta charset="utf-8">
<title>The Lantern Hopper – Book Cover</title>
<link rel="stylesheet" href="https://fonts.googleapis.com/css2?family=Oswald:wght@600&family=Raleway:wght@300&display=swap">
<style>
  :root {
    --page: #ffffff;
    --sky: #d3d8e2;
    --haze: #a9b3c8;
    --sea: #6d7c9e;
    --pool-light: #b4e6ef;
    --pool: #86d3e2;
    --pool-deep: #6cc3d8;
    --title: #4b4a80;
    --logo-grey: #6c6c74;
    --logo-teal: #3fb8bf;
    --author: #ffffff;
  }
  * { margin: 0; padding: 0; box-sizing: border-box; }
  html, body {
    width: 1200px; height: 1200px; overflow: hidden;
    background: var(--page);
  }
  .canvas { position: relative; width: 1200px; height: 1200px; }
  .book-cover {
    position: absolute; left: 300px; top: 168px;
    width: 597px; height: 876px; overflow: hidden;
  }
  .cover-photo {
    position: absolute; inset: 0;
    background: linear-gradient(180deg,
      var(--sky) 0%, var(--haze) 18%, var(--sea) 28%,
      var(--sea) 29.5%, var(--pool-light) 31%,
      var(--pool) 60%, var(--pool-deep) 100%);
  }
  .series-logo {
    position: absolute; left: 190px; top: 40px;
    width: 215px; height: 88px; background: #fff;
    display: flex; align-items: center; gap: 12px; padding: 0 14px;
  }
  .series-logo .mark { width: 40px; height: 40px; background: var(--logo-teal); flex: none; }
  .series-logo .name {
    font-family: "Oswald", sans-serif; font-weight: 600;
    font-size: 22px; line-height: 1.05; color: var(--logo-grey);
  }
  .title {
    position: absolute; left: 0; right: 0; top: 330px;
    text-align: center; color: var(--title);
    font-family: "Oswald", sans-serif; font-weight: 600;
    text-transform: uppercase; line-height: 1;
  }
  .title span { display: block; }
  .title .number { font-size: 128px; letter-spacing: 2px; }
  .title .lead { font-size: 44px; margin-top: 6px; }
  .title .feature { font-size: 92px; margin-top: 6px; letter-spacing: 2px; }
  .title .tail { font-size: 36px; line-height: 1.15; margin-top: 4px; }
  .title .tail + .tail { margin-top: 0; }
  .author {
    position: absolute; left: 0; right: 0; top: 788px;
    text-align: center; color: var(--author);
    font-family: "Raleway", sans-serif; font-weight: 300;
    font-size: 42px; letter-spacing: 2px; text-transform: uppercase;
  }
</style>
</head>
<body>
<div class="canvas">
  <div class="book-cover">
    <div class="cover-photo" role="img" aria-label="Photo of a woman relaxing in an infinity pool overlooking a misty sea"></div>
    <div class="series-logo">
      <div class="mark"></div>
      <div class="name">The Lantern<br>Hopper</div>
    </div>
    <h1 class="title">
      <span class="number">9</span>
      <span class="lead">Bright Paths to Steady</span>
      <span class="feature">Wealth</span>
      <span class="tail">On Your Terms,</span>
      <span class="tail">Leave the Office Grind,</span>
      <span class="tail">and Chase Your Horizon!</span>
    </h1>
    <p class="author">Maren Holloway</p>
  </div>
</div>
</body>
</html>
```